REDESIGN SIGN UP PAGE - EASY TO READ AND UNDERSTAND QUICKLY

I need to redesign my sign up page DESKTOP AND MOBILE VERSION to include 2 products that are each available as a monthly subscription, 6 mth or 12 mth subscription.

Currently I only promote one product on my website but now will be two. https://www.brightlanepromoworks.biz/signup

Now I will have two products:

1. UNLIMITED VACATION CERTIFICATES, DINING VOUCHERS & SAVINGS INCENTIVES
Unlimited Monthly Plan $99 / Month + $199 One-Time Set-Up Fee
Unlimited Bi Annual Plan $490 / 6 Months + $199 One-Time Set-Up Fee
Unlimited Annual Plan $898 / 12 Months + $199 One-Time Set-Up Fee

2. UNLIMITED SMART DEVICE INCENTIVES & OTHER HARD PREMIUMS
Unlimited Monthly Plan $299 / Month + $199 One-Time Set-Up Fee
Unlimited Bi Annual Plan $1,590 / 6 Months + $199 One-Time Set-Up Fee
Unlimited Annual Plan $2,898 / 12 Months + $199 One-Time Set-Up Fee

When promoting the different plans you can see the different categories of incentives I offer here: https://www.brightlanepromoworks.biz/incentives

The SMART DEVICE CERTIFICATES & INCENTIVES category is for product #2 and all the rest of the Categories is for Product #1 Feel free to use images as a visual so customers can see that this product includes Vacations & Restaurants and this product includes only smart devices....

USE ALL CURRENT BULLET POINTS FOR BOTH PLANS THAT IS CURRENTLY ON WEBSITE. USE ALL CURRENT CONTENT ON WEBSITE ORIGINAL SIGN UP PAGE. DO NOT LEAVE ANY CONTENT OUT.

Target Market(s)

BUSINESS OWNERS

Industry/Entity Type

Marketing

Number of Pages Required

2 page

Requirements
Must have
• When promoting the 2 different products on the new sign up page you can see the different categories of incentives I offer here: https://www.brightlanepromoworks.biz/incentives fee; free to use images to showcase what each product offers.

The SMART DEVICE CERTIFICATES & INCENTIVES category is for product #2 and all the rest of the Categories is for Product #1

I want the user to easily understand we have two products that are available in 3 ways, monthly subscription, bi annual and annual and can see the price immediately for all 3 options for both products without toggling, etc.

Must be super clean easy to ready design. Not too busy at all please
Nice to have
• USE ALL CURRENT BULLET POINTS FOR BOTH PLANS THAT IS CURRENTLY ON WEBSITE. USE ALL CURRENT CONTENT ON WEBSITE ORIGINAL SIGN UP PAGE. DO NOT LEAVE ANY CONTENT OUT.

Should not have

```html
<!DOCTYPE html>
<html lang="en">
<head>
<meta charset="utf-8">
<title>Sign Up – Brightlane Promo Works</title>
<link rel="stylesheet" href="https://fonts.googleapis.com/css2?family=Montserrat:wght@400;500;600;700;800&family=Open+Sans:wght@400;600;700&display=swap">
<style>
:root{
  --blue:#1e73be;
  --sky:#42a0ec;
  --orange:#ffaa00;
  --ink:#222;
  --text:#555;
  --muted:#6b6b6b;
  --footer:#000;
  --footer-bar:#3a3a3a;
  --white:#fff;
}
*{box-sizing:border-box;margin:0;padding:0}
html,body{width:1200px;height:2820px;overflow:hidden;background:var(--white)}
body{position:relative;font-family:"Open Sans",sans-serif;color:var(--text)}
a{color:inherit;text-decoration:none}

/* header */
.site-header{position:absolute;left:0;top:0;width:1200px;height:85px;background:var(--white)}
.brand{position:absolute;left:49px;top:22px;display:flex;align-items:center;gap:10px}
.brand-mark{display:block;width:36px;height:36px;background:var(--blue);border-radius:50%}
.brand-name{font-family:"Montserrat",sans-serif;font-weight:700;font-size:16px;color:var(--blue);letter-spacing:.3px;white-space:nowrap}
.main-nav{position:absolute;left:394px;top:36px;display:flex;gap:27px;font-family:"Montserrat",sans-serif;font-weight:600;font-size:12.5px;color:var(--ink)}
.main-nav .active{color:var(--blue);position:relative}
.main-nav .active::after{content:"";position:absolute;left:30px;right:30px;bottom:-8px;height:2px;background:var(--blue)}
.auth{position:absolute;top:25px;display:flex;align-items:center;justify-content:center;height:35px;border:1px solid var(--blue);border-radius:2px;font-family:"Montserrat",sans-serif;font-weight:700;font-size:11px;color:var(--blue)}
.auth.login{left:1016px;width:76px}
.auth.signup{left:1098px;width:76px}

/* hero */
.hero{position:absolute;left:0;top:85px;width:1200px;height:392px;background:linear-gradient(120deg,#6c7480 0%,#3b4350 45%,#22303f 100%)}
.hero-title{position:absolute;left:0;top:130px;width:1200px;text-align:center;font-family:"Montserrat",sans-serif;font-weight:700;font-size:33.5px;line-height:44px;color:var(--white)}

.intro{position:absolute;left:0;top:530px;width:1200px;text-align:center;font-family:"Montserrat",sans-serif;font-size:26px;line-height:35px;color:#333}

/* plans */
.plan{position:absolute;background:var(--white);box-shadow:0 0 8px rgba(0,0,0,.14)}
.plan.monthly{left:100px;top:685px;width:323px;height:877px}
.plan.annual{left:788px;top:685px;width:333px;height:877px}
.plan.biannual{left:423px;top:648px;width:365px;height:984px;z-index:2}
.plan-head{position:relative;color:var(--white);text-align:center}
.monthly .plan-head{height:200px;padding-top:22px;background:linear-gradient(180deg,#6cc0f5,#2f8fe0)}
.annual .plan-head{height:202px;padding-top:28px;background:linear-gradient(180deg,#2e8fdc,#0e55a8)}
.biannual .plan-head{height:222px;padding-top:24px;background:linear-gradient(180deg,#ffc400,#ff9a00)}
.plan-head svg{position:absolute;left:0;bottom:-1px;width:100%;height:24px}
.biannual .plan-head svg{height:26px}
.plan-name{font-family:"Montserrat",sans-serif;font-weight:700;font-size:19px;line-height:21px}
.annual .plan-name{line-height:20px}
.biannual .plan-name{font-size:21px;line-height:23px}
.plan-sub{margin-top:11px;font-size:12.5px;line-height:21px}
.annual .plan-sub{margin-top:6px;line-height:20px}
.biannual .plan-sub{margin-top:12px;font-size:13.5px;line-height:23px}
.plan-price{font-family:"Montserrat",sans-serif;font-weight:700;font-size:44px;line-height:46px}
.annual .plan-price{line-height:52px}
.plan-price sup{font-size:30px;vertical-align:2px}
.biannual .plan-price{font-size:48px;line-height:52px}
.plan-note{font-family:"Montserrat",sans-serif;font-weight:700;font-size:9px;line-height:12px;margin-top:4px}
.biannual .plan-note,.annual .plan-note{margin-top:3px}
.plan-body{padding:24px 0 0 34px}
.annual .plan-body{padding:24px 0 0 30px}
.biannual .plan-body{padding:21px 0 0 23px}
.plan-body h3{font-family:"Montserrat",sans-serif;font-weight:500;font-size:16.5px;line-height:22px;color:var(--ink);margin-left:25px;margin-bottom:12px}
.biannual .plan-body h3{font-size:17.5px;line-height:24px;margin-left:40px;margin-bottom:14px}
.features{list-style:none}
.features li{position:relative;padding-left:25px;font-size:12.3px;line-height:17px;margin-bottom:11.5px;color:var(--muted);white-space:nowrap}
.biannual .features li{padding-left:40px;font-size:13.5px;line-height:18.5px;margin-bottom:12.5px}
.features li svg{position:absolute;left:0;top:4px;width:9px;height:10px}
.biannual .features li svg{left:5px}
.cta{position:absolute;display:flex;align-items:center;justify-content:center;font-family:"Montserrat",sans-serif;font-weight:700;font-size:16px}
.monthly .cta,.annual .cta{left:35px;top:807px;width:270px;height:52px;border:2px solid var(--blue);color:var(--blue);border-radius:2px}
.biannual .cta{left:38px;top:894px;width:290px;height:52px;background:var(--sky);color:var(--white);font-size:17px}

/* products */
.products-title{position:absolute;left:0;top:1690px;width:1200px;text-align:center;font-family:"Montserrat",sans-serif;font-weight:400;font-size:33px;line-height:40px;color:#333;letter-spacing:.5px}
.products-title strong{font-weight:800}
.product{position:absolute;top:1782px;width:509px;height:382px;text-align:center;color:var(--white);padding-top:47px}
.product.leisure{left:90px;background:var(--orange)}
.product.devices{left:621px;background:linear-gradient(135deg,#2a83d8,#1463c4)}
.product h2{font-family:"Montserrat",sans-serif;font-weight:700;font-size:21px;line-height:27px;margin:0 auto 21px}
.price-line{font-family:"Montserrat",sans-serif;font-size:16px;line-height:27px;margin-bottom:12px}
.price-line b{font-weight:700;display:block}
.leisure .price-line span{color:#fff4d6}

/* footer */
.site-footer{position:absolute;left:0;top:2260px;width:1200px;height:467px;background:var(--footer);color:var(--white)}
.foot-brand{position:absolute;left:110px;top:66px;width:230px;text-align:center}
.foot-brand .brand-mark{margin:0 auto 8px;width:32px;height:32px;background:var(--white)}
.foot-brand .brand-name{display:block;color:var(--white);font-size:18px;line-height:22px;white-space:normal}
.social{position:absolute;left:144px;top:181px;display:flex;gap:5px}
.social span{width:37px;height:37px;border:2px solid var(--white);border-radius:50%}
.foot-col{position:absolute;top:72px;font-size:13px;line-height:19.2px;color:var(--white)}
.foot-col h4{font-family:"Montserrat",sans-serif;font-weight:700;font-size:20px;line-height:24px;margin-bottom:8px}
.foot-col p{margin-bottom:19.2px}
.foot-col.contact{left:394px}
.foot-col.quick{left:698px}
.foot-col.other{left:924px}
.foot-col ul{list-style:none}
.foot-bar{position:absolute;left:0;top:2727px;width:1200px;height:93px;background:var(--footer-bar);color:var(--white);font-size:13px}
.foot-bar .copy{position:absolute;left:134px;top:38px}
.foot-bar .legal{position:absolute;right:102px;top:38px}
</style>
</head>
<body>

<header class="site-header">
  <a class="brand" href="#"><span class="brand-mark"></span><span class="brand-name">BRIGHTLANE PROMO WORKS</span></a>
  <nav class="main-nav">
    <a class="active" href="https://www.brightlanepromoworks.biz/incentives">THE INCENTIVES</a>
    <a href="#">SAMPLES</a><a href="#">INDUSTRIES</a><a href="#">TESTIMONIALS</a><a href="#">FAQ</a><a href="#">INTEGRATIONS</a>
  </nav>
  <a class="auth login" href="#">LOGIN</a>
  <a class="auth signup" href="https://www.brightlanepromoworks.biz/signup">SIGN UP</a>
</header>

<section class="hero" role="img" aria-label="Photo of a business team in a meeting, listening to a colleague">
  <h1 class="hero-title">CONGRATULATIONS ON MAKING THE DECISION TO<br>MAKE MORE MONEY FOR YOUR BUSINESS</h1>
</section>

<p class="intro">This program is an online subscription based incentive<br>marketing system with the following features</p>

<article class="plan monthly">
  <div class="plan-head">
    <div class="plan-name">UNLIMITED<br>MONTHLY PLAN</div>
    <div class="plan-sub">One Account Can Be Used For<br>Unlimited Brands</div>
    <div class="plan-price"><sup>$</sup>99</div>
    <div class="plan-note">Month + $199 One-time Set-up fee</div>
    <svg viewBox="0 0 323 24" preserveAspectRatio="none"><path d="M0 24 V16 C60 6 110 4 170 13 C230 22 280 20 323 10 V24 Z" fill="#fff"/></svg>
  </div>
  <div class="plan-body">
    <h3>Unlimited Certificate Types</h3>
    <ul class="features">
      <li><svg viewBox="0 0 9 10"><path d="M2 1 L7 5 L2 9" stroke="#1e73be" stroke-width="1.8" fill="none"/></svg>Unlimited E-Certificates</li>
      <li><svg viewBox="0 0 9 10"><path d="M2 1 L7 5 L2 9" stroke="#1e73be" stroke-width="1.8" fill="none"/></svg>Unlimited SMS Certificates</li>
      <li><svg viewBox="0 0 9 10"><path d="M2 1 L7 5 L2 9" stroke="#1e73be" stroke-width="1.8" fill="none"/></svg>Unlimited Web Banner Certificates</li>
      <li><svg viewBox="0 0 9 10"><path d="M2 1 L7 5 L2 9" stroke="#1e73be" stroke-width="1.8" fill="none"/></svg>Unlimited White Label Certiifcate Landing<br>Pages</li>
      <li><svg viewBox="0 0 9 10"><path d="M2 1 L7 5 L2 9" stroke="#1e73be" stroke-width="1.8" fill="none"/></svg>Unlimited Website Sticky Bar Certificates</li>
      <li><svg viewBox="0 0 9 10"><path d="M2 1 L7 5 L2 9" stroke="#1e73be" stroke-width="1.8" fill="none"/></svg>Unlimited Website Pop Up Certificate</li>
      <li><svg viewBox="0 0 9 10"><path d="M2 1 L7 5 L2 9" stroke="#1e73be" stroke-width="1.8" fill="none"/></svg>Unlimited API E-Certificates</li>
      <li><svg viewBox="0 0 9 10"><path d="M2 1 L7 5 L2 9" stroke="#1e73be" stroke-width="1.8" fill="none"/></svg>Unlimited Flowlink Integration Access</li>
      <li><svg viewBox="0 0 9 10"><path d="M2 1 L7 5 L2 9" stroke="#1e73be" stroke-width="1.8" fill="none"/></svg>FREE Warm Lead Letter Templates</li>
      <li><svg viewBox="0 0 9 10"><path d="M2 1 L7 5 L2 9" stroke="#1e73be" stroke-width="1.8" fill="none"/></svg>FREE Customer Appreciation Letter<br>Templates</li>
      <li><svg viewBox="0 0 9 10"><path d="M2 1 L7 5 L2 9" stroke="#1e73be" stroke-width="1.8" fill="none"/></svg>FREE Professional-Grade Incentive Videos</li>
      <li><svg viewBox="0 0 9 10"><path d="M2 1 L7 5 L2 9" stroke="#1e73be" stroke-width="1.8" fill="none"/></svg>FREE Proven Social Media Ad Templates</li>
      <li><svg viewBox="0 0 9 10"><path d="M2 1 L7 5 L2 9" stroke="#1e73be" stroke-width="1.8" fill="none"/></svg>FREE High-Converting Banner Ad Templates</li>
      <li><svg viewBox="0 0 9 10"><path d="M2 1 L7 5 L2 9" stroke="#1e73be" stroke-width="1.8" fill="none"/></svg>FREE Time-Tested Print Ad Templates</li>
      <li><svg viewBox="0 0 9 10"><path d="M2 1 L7 5 L2 9" stroke="#1e73be" stroke-width="1.8" fill="none"/></svg>FREE White Label Redemption Website</li>
      <li><svg viewBox="0 0 9 10"><path d="M2 1 L7 5 L2 9" stroke="#1e73be" stroke-width="1.8" fill="none"/></svg>FREE Industry Specific Ad Packs</li>
      <li><svg viewBox="0 0 9 10"><path d="M2 1 L7 5 L2 9" stroke="#1e73be" stroke-width="1.8" fill="none"/></svg>FREE Affiliate Program-Earn 50%<br>Commissions</li>
    </ul>
  </div>
  <a class="cta" href="#">GET STARTED</a>
</article>

<article class="plan biannual">
  <div class="plan-head">
    <div class="plan-name">UNLIMITED<br>BI ANNUAL PLAN</div>
    <div class="plan-sub">One Account Can Be Used For<br>Unlimited Brands</div>
    <div class="plan-price"><sup>$</sup>490</div>
    <div class="plan-note">6 Months + $199 One-time Set-up fee</div>
    <svg viewBox="0 0 365 26" preserveAspectRatio="none"><path d="M0 26 V8 C50 18 100 22 180 14 C260 6 320 8 365 20 V26 Z" fill="#fff"/></svg>
  </div>
  <div class="plan-body">
    <h3>Unlimited Certificate Types</h3>
    <ul class="features">
      <li><svg viewBox="0 0 9 10"><path d="M2 1 L7 5 L2 9" stroke="#1e73be" stroke-width="1.8" fill="none"/></svg>Unlimited E-Certificates</li>
      <li><svg viewBox="0 0 9 10"><path d="M2 1 L7 5 L2 9" stroke="#1e73be" stroke-width="1.8" fill="none"/></svg>Unlimited SMS Certificates</li>
      <li><svg viewBox="0 0 9 10"><path d="M2 1 L7 5 L2 9" stroke="#1e73be" stroke-width="1.8" fill="none"/></svg>Unlimited Web Banner Certificates</li>
      <li><svg viewBox="0 0 9 10"><path d="M2 1 L7 5 L2 9" stroke="#1e73be" stroke-width="1.8" fill="none"/></svg>Unlimited White Label Certiifcate Landing<br>Pages</li>
      <li><svg viewBox="0 0 9 10"><path d="M2 1 L7 5 L2 9" stroke="#1e73be" stroke-width="1.8" fill="none"/></svg>Unlimited Website Sticky Bar Certificates</li>
      <li><svg viewBox="0 0 9 10"><path d="M2 1 L7 5 L2 9" stroke="#1e73be" stroke-width="1.8" fill="none"/></svg>Unlimited Website Pop Up Certificate</li>
      <li><svg viewBox="0 0 9 10"><path d="M2 1 L7 5 L2 9" stroke="#1e73be" stroke-width="1.8" fill="none"/></svg>Unlimited API E-Certificates</li>
      <li><svg viewBox="0 0 9 10"><path d="M2 1 L7 5 L2 9" stroke="#1e73be" stroke-width="1.8" fill="none"/></svg>Unlimited Flowlink Integration Access</li>
      <li><svg viewBox="0 0 9 10"><path d="M2 1 L7 5 L2 9" stroke="#1e73be" stroke-width="1.8" fill="none"/></svg>FREE Warm Lead Letter Templates</li>
      <li><svg viewBox="0 0 9 10"><path d="M2 1 L7 5 L2 9" stroke="#1e73be" stroke-width="1.8" fill="none"/></svg>FREE Customer Appreciation Letter<br>Templates</li>
      <li><svg viewBox="0 0 9 10"><path d="M2 1 L7 5 L2 9" stroke="#1e73be" stroke-width="1.8" fill="none"/></svg>FREE Professional-Grade Incentive Videos</li>
      <li><svg viewBox="0 0 9 10"><path d="M2 1 L7 5 L2 9" stroke="#1e73be" stroke-width="1.8" fill="none"/></svg>FREE Proven Social Media Ad Templates</li>
      <li><svg viewBox="0 0 9 10"><path d="M2 1 L7 5 L2 9" stroke="#1e73be" stroke-width="1.8" fill="none"/></svg>FREE High-Converting Banner Ad Templates</li>
      <li><svg viewBox="0 0 9 10"><path d="M2 1 L7 5 L2 9" stroke="#1e73be" stroke-width="1.8" fill="none"/></svg>FREE Time-Tested Print Ad Templates</li>
      <li><svg viewBox="0 0 9 10"><path d="M2 1 L7 5 L2 9" stroke="#1e73be" stroke-width="1.8" fill="none"/></svg>FREE White Label Redemption Website</li>
      <li><svg viewBox="0 0 9 10"><path d="M2 1 L7 5 L2 9" stroke="#1e73be" stroke-width="1.8" fill="none"/></svg>FREE Industry Specific Ad Packs</li>
      <li><svg viewBox="0 0 9 10"><path d="M2 1 L7 5 L2 9" stroke="#1e73be" stroke-width="1.8" fill="none"/></svg>FREE Affiliate Program-Earn 50%<br>Commissions</li>
    </ul>
  </div>
  <a class="cta" href="#">GET STARTED</a>
</article>

<article class="plan annual">
  <div class="plan-head">
    <div class="plan-name">UNLIMITED<br>ANNUAL PLAN</div>
    <div class="plan-sub">One Account Can Be Used For<br>Unlimited Brands</div>
    <div class="plan-price"><sup>$</sup>898</div>
    <div class="plan-note">12 Months + $199 One-time Set-up fee</div>
    <svg viewBox="0 0 333 24" preserveAspectRatio="none"><path d="M0 24 V8 C50 19 110 22 170 14 C230 6 290 6 333 15 V24 Z" fill="#fff"/></svg>
  </div>
  <div class="plan-body">
    <h3>Unlimited Certificate Types</h3>
    <ul class="features">
      <li><svg viewBox="0 0 9 10"><path d="M2 1 L7 5 L2 9" stroke="#1e73be" stroke-width="1.8" fill="none"/></svg>Unlimited E-Certificates</li>
      <li><svg viewBox="0 0 9 10"><path d="M2 1 L7 5 L2 9" stroke="#1e73be" stroke-width="1.8" fill="none"/></svg>Unlimited SMS Certificates</li>
      <li><svg viewBox="0 0 9 10"><path d="M2 1 L7 5 L2 9" stroke="#1e73be" stroke-width="1.8" fill="none"/></svg>Unlimited Web Banner Certificates</li>
      <li><svg viewBox="0 0 9 10"><path d="M2 1 L7 5 L2 9" stroke="#1e73be" stroke-width="1.8" fill="none"/></svg>Unlimited White Label Certiifcate Landing<br>Pages</li>
      <li><svg viewBox="0 0 9 10"><path d="M2 1 L7 5 L2 9" stroke="#1e73be" stroke-width="1.8" fill="none"/></svg>Unlimited Website Sticky Bar Certificates</li>
      <li><svg viewBox="0 0 9 10"><path d="M2 1 L7 5 L2 9" stroke="#1e73be" stroke-width="1.8" fill="none"/></svg>Unlimited Website Pop Up Certificate</li>
      <li><svg viewBox="0 0 9 10"><path d="M2 1 L7 5 L2 9" stroke="#1e73be" stroke-width="1.8" fill="none"/></svg>Unlimited API E-Certificates</li>
      <li><svg viewBox="0 0 9 10"><path d="M2 1 L7 5 L2 9" stroke="#1e73be" stroke-width="1.8" fill="none"/></svg>Unlimited Flowlink Integration Access</li>
      <li><svg viewBox="0 0 9 10"><path d="M2 1 L7 5 L2 9" stroke="#1e73be" stroke-width="1.8" fill="none"/></svg>FREE Warm Lead Letter Templates</li>
      <li><svg viewBox="0 0 9 10"><path d="M2 1 L7 5 L2 9" stroke="#1e73be" stroke-width="1.8" fill="none"/></svg>FREE Customer Appreciation Letter<br>Templates</li>
      <li><svg viewBox="0 0 9 10"><path d="M2 1 L7 5 L2 9" stroke="#1e73be" stroke-width="1.8" fill="none"/></svg>FREE Professional-Grade Incentive Videos</li>
      <li><svg viewBox="0 0 9 10"><path d="M2 1 L7 5 L2 9" stroke="#1e73be" stroke-width="1.8" fill="none"/></svg>FREE Proven Social Media Ad Templates</li>
      <li><svg viewBox="0 0 9 10"><path d="M2 1 L7 5 L2 9" stroke="#1e73be" stroke-width="1.8" fill="none"/></svg>FREE High-Converting Banner Ad Templates</li>
      <li><svg viewBox="0 0 9 10"><path d="M2 1 L7 5 L2 9" stroke="#1e73be" stroke-width="1.8" fill="none"/></svg>FREE Time-Tested Print Ad Templates</li>
      <li><svg viewBox="0 0 9 10"><path d="M2 1 L7 5 L2 9" stroke="#1e73be" stroke-width="1.8" fill="none"/></svg>FREE White Label Redemption Website</li>
      <li><svg viewBox="0 0 9 10"><path d="M2 1 L7 5 L2 9" stroke="#1e73be" stroke-width="1.8" fill="none"/></svg>FREE Industry Specific Ad Packs</li>
      <li><svg viewBox="0 0 9 10"><path d="M2 1 L7 5 L2 9" stroke="#1e73be" stroke-width="1.8" fill="none"/></svg>FREE Affiliate Program-Earn 50%<br>Commissions</li>
    </ul>
  </div>
  <a class="cta" href="#">GET STARTED</a>
</article>

<h2 class="products-title">OUR <strong>PRODUCTS</strong></h2>

<section class="product leisure">
  <h2>UNLIMITED VACATION CERTIFICATES,<br>DINING VOUCHERS &amp; SAVINGS<br>INCENTIVES</h2>
  <p class="price-line"><b>Unlimited Monthly Plan $99 / Month + $199</b><span>One-Time Set-Up Fee</span></p>
  <p class="price-line"><b>Unlimited Bi Annual Plan $490 / 6 Months + $199</b><span>One-Time Set-Up Fee</span></p>
  <p class="price-line"><b>Unlimited Annual Plan $898 / 12 Months + $199</b><span>One-Time Set-Up Fee</span></p>
</section>

<section class="product devices" aria-label="Blue panel with a faint background image of smart devices">
  <h2>UNLIMITED SMART DEVICE<br>INCENTIVES &amp; OTHER HARD<br>PREMIUMS</h2>
  <p class="price-line"><b>Unlimited Monthly Plan $299 / Month + $199</b><span>One-Time Set-Up Fee</span></p>
  <p class="price-line"><b>Unlimited Bi Annual Plan $1,590 / 6 Months + $199</b><span>One-Time Set-Up Fee</span></p>
  <p class="price-line"><b>Unlimited Annual Plan $2,898 / 12 Months + $199</b><span>One-Time Set-Up Fee</span></p>
</section>

<footer class="site-footer">
  <div class="foot-brand"><span class="brand-mark"></span><span class="brand-name">BRIGHTLANE<br>PROMO WORKS</span></div>
  <div class="social" aria-label="Social links"><span></span><span></span><span></span><span></span></div>
  <div class="foot-col contact">
    <h4>CONTACT US</h4>
    <p><b>Brightlane Promo Works Group, Inc.</b><br>4470 Harborview Lane Suite 120<br>Seaport City, CA 90000</p>
    <p>USA Office: 1-555-301-2200<br>International: 1-800-555-0148<br>Text Us: 1-555-301-2299</p>
    <p>info@brightlanepromoworks.biz</p>
    <p>24/7 Chat Support<br>24/7 Live Answering Service<br>24/7 Email Support<br>Live Phone &amp; SMS Support:<br>Monday - Friday 8am - 5pm PST<br>Sat/Sun/Holidays Closed</p>
  </div>
  <div class="foot-col quick">
    <h4>QUICK LINKS</h4>
    <ul><li>Home</li><li>The Incentives</li><li>Samples</li><li>Affiliate</li><li>Testimonials</li><li>Faq</li><li>Contact Us</li><li>Redemption Demo Videos</li><li>BPW Distribute</li><li>Certificate Demo Videos</li></ul>
  </div>
  <div class="foot-col other">
    <h4>OTHER LINKS</h4>
    <ul><li>Hoteliers</li><li>BPW Certificates List</li><li>How To Use BPW Certificates</li><li>Social Media Incentive Campaign</li><li>Pop Ups &amp; Sticky Bars</li><li>Whitepaper - Increase Sales</li><li>Whitepaper - Improve Sales</li><li>During Strange Times</li><li>Whitepaper - Boost Website</li><li>Conversions</li></ul>
  </div>
</footer>
<div class="foot-bar">
  <span class="copy">© 2020 Brightlane Promo Works Group, Inc. | All Rights Reserved.</span>
  <span class="legal">Privacy Policy &nbsp;|&nbsp; Term And Conditions</span>
</div>

</body>
</html>
```